Design a website for a quickly growing ghostwriting and editing firm

NRB Productions has a website through Wix, but we need help! We are based in Austin, TX, and we work primarily with self-help, wellness, and diet authors. We offer ghostwriting, editing and book development services. You can see our basic site now at www.nadiabrentproductions.example

```html
<!DOCTYPE html>
<html lang="en">
<head>
<meta charset="utf-8">
<title>NRB Productions</title>
<link rel="stylesheet" href="https://fonts.googleapis.com/css2?family=Quicksand:wght@500;600;700&family=Roboto:wght@400;500;700&display=swap">
<style>
:root{
  --amber:#c8822f;
  --ink:#111111;
  --body:#555555;
  --mist:#f0f0f0;
  --white:#ffffff;
  --night:#000000;
}
*{margin:0;padding:0;box-sizing:border-box}
html,body{width:1200px;height:3147px;overflow:hidden}
body{position:relative;background:var(--white);font-family:'Roboto',sans-serif;color:var(--ink)}
.abs{position:absolute}
.heading{font-family:'Quicksand',sans-serif;font-weight:700;text-align:center;color:var(--ink);letter-spacing:.5px}
.btn{position:absolute;background:var(--amber);color:var(--white);border-radius:22px;font-weight:700;font-size:14px;display:flex;align-items:center;justify-content:center;text-transform:uppercase}
.wordmark{font-family:'Quicksand',sans-serif;font-weight:600;font-size:20px;display:flex;align-items:center;gap:10px;white-space:nowrap}
.wordmark .dot{width:40px;height:40px;border-radius:50%;background:var(--amber);flex:none}
/* header */
.site-header{top:0;left:0;width:1200px;height:88px;background:var(--white)}
.site-header .wordmark{position:absolute;left:111px;top:22px;color:#333}
.nav{position:absolute;left:446px;top:0;display:flex;height:63px;align-items:center;font-size:14px;font-weight:500}
.nav a{color:var(--ink);text-decoration:none;margin-right:33px}
.nav a.active{background:var(--amber);color:var(--white);height:63px;padding:0 14px;display:flex;align-items:center;padding-top:20px;margin-right:20px}
/* hero */
.hero{top:88px;left:0;width:1200px;height:700px}
.hero-title{position:absolute;left:520px;top:168px;font-family:'Quicksand',sans-serif;font-weight:700;font-size:68px;line-height:68px;color:var(--white);text-transform:uppercase}
.dots{position:absolute;left:578px;top:599px;display:flex;gap:5px}
.dots span{width:12px;height:12px;border-radius:50%;border:2px solid var(--white)}
.dots span.on{background:var(--white)}
/* work with */
.work-title{top:866px;left:0;width:1200px;font-size:35px}
.focus{position:absolute;top:943px;width:310px;text-align:center}
.focus .ring{width:304px;height:304px;border-radius:50%;border:3px solid var(--amber);margin:0 auto;padding:12px}
.focus .ring div{width:100%;height:100%;border-radius:50%}
.focus h3{font-family:'Quicksand',sans-serif;font-weight:700;font-size:21px;margin-top:18px;letter-spacing:.5px}
.focus p{font-size:13.5px;line-height:22px;color:var(--body);margin-top:12px;padding:0 20px}
/* who we are */
.about{top:1460px;left:0;width:1200px;height:570px}
.about-text{position:absolute;top:1578px;left:210px;width:780px;text-align:center}
.about-text h2{font-size:34px}
.about-text p{font-size:13.5px;line-height:22px;color:var(--body);margin-top:18px}
.about-text p+p{margin-top:22px}
/* services */
.services-title{top:2112px;left:0;width:1200px;font-size:35px}
.card{position:absolute;top:2186px;width:324px;height:404px;background:var(--mist);border-radius:36px;text-align:center;overflow:hidden}
.card .photo{position:absolute;left:0;width:324px;height:240px;border:5px solid var(--amber);border-radius:36px}
.card .badge{position:absolute;left:114px;width:96px;height:96px;border-radius:50%;background:var(--amber);display:flex;align-items:center;justify-content:center}
.card h3{position:absolute;left:0;width:100%;font-family:'Quicksand',sans-serif;font-weight:700;font-size:21px;letter-spacing:.5px}
.card p{position:absolute;left:30px;width:264px;font-size:13.5px;line-height:22px;color:var(--body)}
/* footer */
.footer{top:2680px;left:0;width:1200px;height:467px}
.footer-brand{left:111px;top:2853px;color:var(--white)}
.socials{position:absolute;left:124px;top:2930px;display:flex;gap:5px}
.socials span{width:35px;height:35px;border-radius:50%;background:var(--white)}
.f-col{position:absolute;top:2848px;color:var(--white)}
.f-col h4{font-size:21px;font-weight:700}
.f-col ul{list-style:none;margin-top:20px;font-size:13.5px;line-height:22.5px}
.f-col li{display:flex;align-items:flex-start;gap:9px}
.chev{color:var(--amber);font-size:12px}
.contact-list li{margin-bottom:11px;line-height:22px}
.email-field{position:absolute;left:858px;top:2896px;width:230px;height:33px;border-bottom:1px solid #bbb;color:#bbb;font-size:13.5px;padding:8px 8px}
.footer-rule{top:3063px;left:111px;width:977px;height:1px;background:#333}
.copyright{top:3089px;left:0;width:1200px;text-align:center;color:var(--white);font-size:12.5px}
</style>
</head>
<body>

<header class="site-header abs">
  <div class="wordmark"><span class="dot"></span>NRB PRODUCTIONS</div>
  <nav class="nav">
    <a class="active">HOME</a><a>ABOUT US</a><a>SERVICES</a><a>BLOG</a><a>CONTACT US</a>
  </nav>
  <div class="btn" style="left:938px;top:21px;width:150px;height:43px">Get a Quote</div>
</header>

<section class="hero abs">
  <svg class="abs" style="top:0;left:0" width="1200" height="700" viewBox="0 88 1200 700">
    <defs>
      <linearGradient id="sunset" x1="0" y1="0" x2="1" y2="1">
        <stop offset="0" stop-color="#6a4a3a"/>
        <stop offset="0.45" stop-color="#d99a45"/>
        <stop offset="0.75" stop-color="#f2c46a"/>
        <stop offset="1" stop-color="#8a6a3a"/>
      </linearGradient>
    </defs>
    <path d="M0 88 H1200 V610 Q600 905 0 680 Z" fill="var(--amber)"/>
    <path d="M0 88 H1200 V598 Q600 905 0 640 Z" fill="url(#sunset)" role="img" aria-label="Photo of a couple sitting on a rocky summit above a bay at sunset"/>
  </svg>
  <h1 class="hero-title">Nadia Brent<br>Productions</h1>
  <div class="btn" style="left:523px;top:315px;width:150px;height:43px">Get Started</div>
  <div class="dots"><span></span><span class="on"></span><span></span></div>
</section>

<h2 class="heading abs work-title">WE WORK WITH US</h2>
<div class="focus" style="left:105px">
  <div class="ring"><div role="img" aria-label="Photo of a support group seated in a circle" style="background:linear-gradient(160deg,#b79a82,#5a6a8a)"></div></div>
  <h3>SELF-HELP</h3>
  <p>Lorem ipsum dolor sit amet, conse ctetur adipiscing elit, sed do eiusmod tempor incididunt ut</p>
</div>
<div class="focus" style="left:445px">
  <div class="ring"><div role="img" aria-label="Photo of hands forming a heart shape" style="background:linear-gradient(160deg,#6e6a7c,#c2a9a0)"></div></div>
  <h3>WELLNESS</h3>
  <p>Lorem ipsum dolor sit amet, conse ctetur adipiscing elit, sed do eiusmod tempor incididunt ut</p>
</div>
<div class="focus" style="left:784px">
  <div class="ring"><div role="img" aria-label="Photo of a stack of books with a quill and inkwell" style="background:linear-gradient(160deg,#4a5a54,#b99a68)"></div></div>
  <h3>DIET AUTHORS</h3>
  <p>Lorem ipsum dolor sit amet, conse ctetur adipiscing elit, sed do eiusmod tempor incididunt ut</p>
</div>

<section class="about abs">
  <svg class="abs" style="top:0;left:0" width="1200" height="570" viewBox="0 0 1200 570">
    <defs>
      <linearGradient id="pages" x1="0" y1="0" x2="0" y2="1">
        <stop offset="0" stop-color="#e6e6e6"/>
        <stop offset="0.6" stop-color="#f4f4f4"/>
        <stop offset="1" stop-color="#dcdcdc"/>
      </linearGradient>
    </defs>
    <path d="M0 150 Q600 -119 1200 120 V410 Q600 700 0 430 Z" fill="var(--amber)"/>
    <path d="M0 145 Q600 -123 1200 190 V400 Q600 701 0 390 Z" fill="url(#pages)" role="img" aria-label="Faded photo of an open book"/>
  </svg>
</section>
<div class="about-text">
  <h2 class="heading">WHO WE ARE</h2>
  <p>Lorem ipsum dolor sit amet, consectetur adipiscing elit, sed do eiusmod tempor incididunt ut labore et dolore magna aliqua. Ut enim ad minim veniam, quis nostrud exercitation ullamco laboris nisi ut aliquip ex ea commodo consequat. Duis aute irure dolor in reprehenderit in voluptate velit esse cillum dolore eu fugiat nulla pariatur. Excepteur sint occaecat cupidatat non proident, sunt in culpa qui officia deserunt mollit anim id est laborum.</p>
  <p>Lorem ipsum dolor sit amet, consectetur adipiscing elit, sed do eiusmod tempor incididunt ut labore et dolore magna aliqua. Ut enim ad minim veniam, quis nostrud exercitation ullamco laboris nisi ut aliquip ex ea commodo consequat. Duis aute irure dolor in reprehenderit in voluptate velit esse cillum dolore eu fugiat nulla pariatur. Excepteur sint occaecat cupidatat non proident, sunt in culpa qui officia deserunt mollit anim id est laborum.</p>
</div>
<div class="btn" style="left:523px;top:1865px;width:150px;height:43px">Get Started</div>

<h2 class="heading abs services-title">OUR SERVICES</h2>

<div class="card" style="left:111px">
  <div class="photo" role="img" aria-label="Photo of a candle, cross and old scrolls with a quill" style="top:0;background:linear-gradient(150deg,#2a1d12,#8a6a40,#1a120a)"></div>
  <div class="badge" style="top:145px">
    <svg width="52" height="52" viewBox="0 0 52 52" fill="none" stroke="#fff" stroke-width="2.2" stroke-linejoin="round"><path d="M12 10 H34 V42 H12 Z"/><path d="M17 18 H29 M17 24 H29 M17 30 H25"/><path d="M42 14 L28 36 L25 40 L26 35 L40 12 Z"/></svg>
  </div>
  <h3 style="top:262px">GHOSTWRITING</h3>
  <p style="top:306px">Lorem ipsum dolor sit amet, conse ctetur adipiscing elit, sed do eiusmod tempor incididunt ut</p>
</div>

<div class="card" style="left:438px">
  <h3 style="top:34px">EDITING</h3>
  <p style="top:76px">Lorem ipsum dolor sit amet, conse ctetur adipiscing elit, sed do eiusmod tempor incididunt ut</p>
  <div class="photo" role="img" aria-label="Photo of a video editing desk with monitors" style="top:164px;background:linear-gradient(150deg,#7a5a3a,#c09060,#2a2a32)"></div>
  <div class="badge" style="top:167px">
    <svg width="52" height="52" viewBox="0 0 52 52" fill="none" stroke="#fff" stroke-width="2.2" stroke-linejoin="round"><path d="M10 16 H34 V42 H10 Z"/><path d="M14 20 V38 M30 20 V38"/><path d="M44 10 L26 32 L23 36 L24 31 L42 8 Z"/></svg>
  </div>
</div>

<div class="card" style="left:764px">
  <div class="photo" role="img" aria-label="Photo of stacked books with a magnifying glass" style="top:0;background:linear-gradient(160deg,#2e4a50,#5a6a6e,#8a4a3a)"></div>
  <div class="badge" style="top:145px">
    <svg width="52" height="52" viewBox="0 0 52 52" fill="none" stroke="#fff" stroke-width="2.2"><circle cx="26" cy="24" r="13"/><circle cx="26" cy="24" r="6"/><path d="M26 6 V11 M26 37 V42 M8 24 H13 M39 24 H44 M13 11 L17 15 M35 33 L39 37 M39 11 L35 15 M17 33 L13 37"/><path d="M18 46 H34"/></svg>
  </div>
  <h3 style="top:262px">BOOK DEVELOPMENT</h3>
  <p style="top:306px">Lorem ipsum dolor sit amet, conse ctetur adipiscing elit, sed do eiusmod tempor incididunt ut</p>
</div>

<footer class="footer abs">
  <svg class="abs" style="top:0;left:0" width="1200" height="467" viewBox="0 0 1200 467">
    <path d="M0 160 Q600 -120 1200 120 V467 H0 Z" fill="var(--amber)"/>
    <path d="M0 165 Q600 -117 1200 170 V467 H0 Z" fill="var(--night)"/>
  </svg>
</footer>
<div class="abs wordmark footer-brand"><span class="dot"></span>NRB PRODUCTIONS</div>
<div class="socials"><span></span><span></span><span></span><span></span></div>

<div class="f-col" style="left:387px">
  <h4>Quick links</h4>
  <ul>
    <li><span class="chev">»</span>Home</li>
    <li><span class="chev">»</span>About us</li>
    <li><span class="chev">»</span>Services</li>
    <li><span class="chev">»</span>Applications</li>
    <li><span class="chev">»</span>Contact us</li>
  </ul>
</div>

<div class="f-col" style="left:575px">
  <h4>Contact us</h4>
  <ul class="contact-list">
    <li><svg width="16" height="18" viewBox="0 0 16 18"><path d="M8 1 C4 1 2 4 2 6.5 C2 10 8 16 8 16 C8 16 14 10 14 6.5 C14 4 12 1 8 1 Z" fill="var(--amber)"/><circle cx="8" cy="6.5" r="2" fill="#000"/></svg><span>Lorem ipsum dolor sit<br>amet, consectetur</span></li>
    <li style="margin-bottom:0"><svg width="16" height="18" viewBox="0 0 16 16"><path d="M3 2 L6 2 L7 5 L5 6.5 C6 9 7 10 9.5 11 L11 9 L14 10 L14 13 C14 14 13 15 12 15 C6 14 2 10 1 4 C1 3 2 2 3 2 Z" fill="var(--amber)"/></svg>+1 888 888 8888</li>
    <li><svg width="16" height="18" viewBox="0 0 16 16"><rect x="1" y="3" width="14" height="10" fill="var(--amber)"/><path d="M1 3 L8 9 L15 3" fill="none" stroke="#000" stroke-width="1.4"/></svg>info@companyname.com</li>
  </ul>
</div>

<div class="f-col" style="left:858px">
  <h4>Newsletter</h4>
</div>
<div class="email-field">Email address</div>
<div class="btn" style="left:858px;top:2946px;width:158px;height:49px;border-radius:25px">Submit</div>

<div class="abs footer-rule"></div>
<div class="abs copyright">© Copyrights Company name 2021. All rights reserved | Privacy policy | Terms Condition</div>

</body>
</html>
```